The Perfect Business Card for PineHarbor

I am looking for a business card which beautifully incorporates my logo, reflects my business and looks special, elegant and clean.

```html
<!DOCTYPE html>
<html lang="de">
<head>
<meta charset="utf-8">
<title>PineHarbor – Visitenkarte</title>
<link href="https://fonts.googleapis.com/css2?family=Crimson+Text:wght@600&family=Great+Vibes&display=swap" rel="stylesheet">
<style>
  :root {
    --stage: #444446;
    --olive: #a3b23a;
    --olive-deep: #8fa12c;
    --front-top: #b2bd3e;
    --front-mid: #9fb43f;
    --front-bottom: #7fae3c;
    --back-light: #f6f9f0;
    --back-tint: #e9f1dc;
    --white: #ffffff;
  }
  html, body {
    margin: 0;
    padding: 0;
    width: 1200px;
    height: 1200px;
    overflow: hidden;
    background: var(--stage);
  }
  .canvas {
    position: relative;
    width: 1200px;
    height: 1200px;
    font-family: "Crimson Text", Georgia, serif;
    font-weight: 600;
  }
  .card {
    position: absolute;
    left: 224px;
    width: 734px;
    height: 448px;
    border-radius: 30px;
    overflow: hidden;
  }
  /* Front */
  .card-front { top: 138px; }
  .front-photo {
    position: absolute;
    inset: 0;
    background:
      radial-gradient(ellipse at 70% 75%, rgba(120,170,60,0.55), transparent 60%),
      linear-gradient(160deg, var(--front-top) 0%, var(--front-mid) 55%, var(--front-bottom) 100%);
  }
  .front-brand {
    position: absolute;
    left: 0;
    right: 0;
    top: 180px;
    display: flex;
    align-items: center;
    justify-content: center;
    gap: 18px;
    color: var(--white);
  }
  .brand-dot {
    width: 14px;
    height: 14px;
    border-radius: 50%;
    background: var(--white);
  }
  .brand-name {
    font-size: 76px;
    line-height: 1;
    letter-spacing: 2px;
    text-transform: uppercase;
  }
  /* Back */
  .card-back {
    top: 633px;
    background:
      radial-gradient(ellipse at 80% 30%, var(--back-tint), transparent 55%),
      radial-gradient(ellipse at 20% 80%, var(--back-tint), transparent 50%),
      var(--back-light);
    color: var(--olive);
  }
  .person-name {
    position: absolute;
    left: 42px;
    top: 58px;
    font-family: "Great Vibes", cursive;
    font-weight: 400;
    font-size: 50px;
    line-height: 1.2;
    color: var(--olive);
  }
  .qualifications {
    position: absolute;
    left: 42px;
    top: 166px;
    margin: 0;
    padding: 0 0 0 23px;
    font-size: 16.5px;
    line-height: 22px;
  }
  .qualifications li { padding-left: 2px; }
  .contact-list {
    position: absolute;
    left: 42px;
    top: 326px;
    margin: 0;
    padding: 0;
    list-style: none;
    font-size: 24px;
    line-height: 24px;
  }
  .contact-list li {
    display: flex;
    align-items: center;
    gap: 14px;
  }
  .contact-list svg { width: 24px; height: 20px; flex: none; }
  .divider {
    position: absolute;
    left: 340px;
    top: 335px;
    width: 4px;
    height: 64px;
    background: var(--olive);
  }
  .address {
    position: absolute;
    left: 384px;
    top: 343px;
    display: flex;
    align-items: center;
    gap: 14px;
  }
  .address svg { width: 34px; height: 48px; flex: none; }
  .address p {
    margin: 0;
    font-size: 20px;
    line-height: 29px;
    text-transform: uppercase;
    letter-spacing: 0.5px;
  }
  .back-brand {
    position: absolute;
    left: 440px;
    top: 150px;
    width: 250px;
    display: flex;
    align-items: center;
    justify-content: center;
    gap: 12px;
    color: var(--olive);
  }
  .back-brand .brand-dot { background: var(--olive); width: 12px; height: 12px; }
  .back-brand .brand-name { font-size: 34px; }
</style>
</head>
<body>
<main class="canvas">

  <section class="card card-front">
    <div class="front-photo" role="img" aria-label="Green-toned photo of a woman lying in the grass holding a dandelion"></div>
    <div class="front-brand">
      <span class="brand-dot"></span>
      <span class="brand-name">PineHarbor</span>
    </div>
  </section>

  <section class="card card-back">
    <h1 class="person-name">Dr. Mara Lindqvist</h1>

    <ul class="qualifications">
      <li>Arbeits-und Organisationspsychologin,Dipl.</li>
      <li>Coach, Dipl.</li>
      <li>Hypnosetherapeutin, Dipl.</li>
      <li>Naturheilpraktikerin (TEN), Dipl.</li>
      <li>Ayurveda Therapeutin,</li>
      <li>Ayuryoga Yogatherapeutin.</li>
    </ul>

    <div class="back-brand">
      <span class="brand-dot"></span>
      <span class="brand-name">PineHarbor</span>
    </div>

    <ul class="contact-list">
      <li>
        <svg viewBox="0 0 24 24" aria-hidden="true"><path fill="currentColor" d="M6.6 2.5l3 3.6-1.8 2.3c1.2 2.6 3.2 4.6 5.8 5.8l2.3-1.8 3.6 3-1.6 3.1c-.4.7-1.2 1-2 .8C9 17.7 4.3 13 2.7 6.1c-.2-.8.1-1.6.8-2z"/></svg>
        <span>+41 (0) 76 000 1234</span>
      </li>
      <li>
        <svg viewBox="0 0 24 18" aria-hidden="true"><rect x="1" y="1" width="22" height="16" fill="none" stroke="currentColor" stroke-width="2"/><path d="M1 1l11 9 11-9M1 17l8-7M23 17l-8-7" fill="none" stroke="currentColor" stroke-width="2"/></svg>
        <span>mara@pineharbor.ch</span>
      </li>
      <li>
        <svg viewBox="0 0 24 24" aria-hidden="true"><circle cx="12" cy="12" r="10" fill="none" stroke="currentColor" stroke-width="2"/><path d="M2 12h20M12 2c3 3 3 17 0 20M12 2c-3 3-3 17 0 20" fill="none" stroke="currentColor" stroke-width="1.6"/></svg>
        <span>www.pineharbor.ch</span>
      </li>
    </ul>

    <div class="divider"></div>

    <div class="address">
      <svg viewBox="0 0 24 34" aria-hidden="true"><path fill="currentColor" d="M12 0C5.4 0 0 5.2 0 11.7 0 20 12 34 12 34s12-14 12-22.3C24 5.2 18.6 0 12 0zm0 16.5a5 5 0 110-10 5 5 0 010 10z"/></svg>
      <p>Birkenweg 7,<br>8003 Zürich | Schweiz</p>
    </div>
  </section>

</main>
</body>
</html>
```